Hedge Fund Business Presentation for prospective clients

We need a professional design for our PowerPoint presentation that we use to send to prospective clients for our Alternative Investments/Hedge Fund. This presentation needs to have the same verbiage as what is being used already. We will present this to individuals, institutions (banks, non profits), and to Registered Investment Advisors that have client money to place.

Target Market(s)

High net worth individuals, high income earners, doctors, lawyers, business owners, sophisticated investors

Industry/Entity Type

Investment Advisory

Other font styles liked:
• font that is in logo

Requirements
Must have
• a very simple, but professional, elegant design. must include our color scheme, feel free to add other shades in our scheme.

```html
<!DOCTYPE html>
<html lang="en">
<head>
<meta charset="utf-8">
<title>Halvern Ridge – Investor Presentation</title>
<link href="https://fonts.googleapis.com/css2?family=Roboto+Condensed:wght@400;700&family=Roboto:wght@400;700&display=swap" rel="stylesheet">
<style>
:root{
  --ink:#0b0b0b;
  --brand:#2a86e8;
  --brand-deep:#1469d4;
  --label:#1b78de;
  --pale:#bfe3f6;
  --pale-soft:#e6f4fb;
  --text:#1d1d1d;
  --frame:#2a2a2a;
  --page:#ffffff;
}
*{box-sizing:border-box;margin:0;padding:0}
html,body{width:1200px;height:700px;overflow:hidden;background:var(--page)}
body{font-family:"Roboto",Arial,sans-serif;color:var(--text);position:relative}
.slide{position:absolute;width:392px;height:222px;background:#fff;border:1.5px solid var(--frame);overflow:hidden}
.slide-head{position:absolute;left:0;top:0;right:0;height:36px;background:var(--ink)}
.slide-head::before{content:"";position:absolute;left:0;top:0;width:32px;height:36px;background:var(--brand)}
.slide-title{position:absolute;left:46px;top:0;line-height:36px;color:#fff;font-family:"Roboto Condensed",sans-serif;font-size:13.5px;font-weight:400;white-space:nowrap}
.slide-title small{font-size:9.5px}
.foot-name{position:absolute;right:30px;bottom:6px;font-family:"Roboto Condensed",sans-serif;font-size:6px;color:var(--brand-deep);letter-spacing:.5px}
.page-no{position:absolute;right:0;bottom:0;width:16px;height:17px;background:var(--brand);color:#fff;font-size:7px;text-align:center;line-height:17px}
.slide::after{content:"";position:absolute;left:0;right:16px;bottom:0;height:1.5px;background:var(--brand)}
.cover::after{display:none}
.label{font-family:"Roboto Condensed",sans-serif;color:var(--label);font-size:8px;font-weight:400;text-transform:uppercase}
.label-rule{border-bottom:1.2px solid var(--label);padding-bottom:2px;display:inline-block}
.body{font-size:7px;line-height:1.32}
.pale-box{background:var(--pale)}
.abs{position:absolute}
.brand-name{font-family:"Roboto Condensed",sans-serif;color:var(--brand-deep);font-weight:400;letter-spacing:2px}

/* cover */
.cover-art{position:absolute;left:120px;top:24px;width:270px;height:166px;background:linear-gradient(180deg,#eaf6fb 0%,#cfe9f4 100%)}
.cover-corner{position:absolute;left:0;top:0;width:33px;height:36px;background:var(--brand)}
.cover-band{position:absolute;left:0;right:0;bottom:0;height:38px;background:var(--ink);color:#fff;text-align:center;line-height:38px;font-family:"Roboto Condensed",sans-serif;font-size:10.5px}
.cover-name{position:absolute;left:50px;top:62px;font-size:14px}

.card{position:absolute;border:1.3px solid var(--label);padding:5px 6px;font-size:7px;line-height:1.3}
.card .label{font-weight:700;font-size:7.5px;text-decoration:underline}

.quote-list p{margin-bottom:3px}
.chart-text{font-family:"Roboto Condensed",sans-serif;font-weight:700;font-size:6.3px;text-align:center;color:#111;line-height:1.15}
.org-box{position:absolute;background:var(--pale);text-align:center;font-family:"Roboto Condensed",sans-serif;font-weight:700;font-size:6.2px;line-height:1.5;padding:4px 3px}
.bullets{position:absolute;font-size:6px;line-height:1.2;list-style:none}
.bullets li{padding-left:6px;position:relative;margin-bottom:1.5px}
.bullets li::before{content:"";position:absolute;left:0;top:2px;width:3.5px;height:3.5px;border-radius:50%;background:var(--label)}
.rationale-box{position:absolute;border:1.3px solid var(--label);color:var(--label);text-align:center;font-family:"Roboto Condensed",sans-serif;font-size:8.3px;line-height:1.45;background:#fff}
.rationale-sub{position:absolute;background:var(--pale);text-align:center;font-family:"Roboto Condensed",sans-serif;font-size:7.8px;line-height:1.55;color:#1d3f55}
.deco{position:absolute;background:radial-gradient(circle at 70% 55%,#dcf0f8 0%,#eef8fc 45%,#fff 80%)}
.stage-head{position:absolute;font-family:"Roboto Condensed",sans-serif;font-weight:700;font-size:8px}
.stage-box{position:absolute;background:var(--pale);font-size:5.6px;line-height:1.25;padding:4px 5px}
.stage-box p{margin-bottom:3px}
</style>
</head>
<body>

<!-- 1 Cover -->
<section class="slide cover" style="left:4px;top:6px">
  <div class="cover-art" role="img" aria-label="Pale blue line illustration of a fortified stone city wall with towers"></div>
  <div class="cover-corner"></div>
  <div class="brand-name cover-name">HALVERN RIDGE</div>
  <div class="cover-band">Prudence in Planning. Vigilance in Execution.</div>
</section>

<!-- 2 Managing Members -->
<section class="slide" style="left:404px;top:6px">
  <div class="slide-head"><h2 class="slide-title">Managing Members</h2></div>
  <div class="card" style="left:38px;top:69px;width:121px;height:55px">
    <div class="label">OWEN R. TALBERT</div>
    <div style="margin-top:3px">Co-Founder &amp; Managing Member<br>Phone: 555.204.7310<br>Owen@HalvernRidge.com</div>
  </div>
  <div class="card" style="left:225px;top:68px;width:122px;height:55px">
    <div class="label">LUCAS D. BRENNER</div>
    <div style="margin-top:3px">Co-Founder &amp; Managing Member<br>Phone: 555.318.6627<br>Lucas@HalvernRidge.com</div>
  </div>
  <div class="abs body" style="left:50px;top:157px;font-size:6px;line-height:1.35">
    <span class="label" style="font-size:6.3px;text-transform:none;font-weight:700">Halvern Ridge, LLC</span><br>
    48 Alder Court | Fairhaven ST 00000<br>Office: 555.204.7310
  </div>
  <div class="abs" style="left:197px;top:159px;width:1.2px;height:22px;background:var(--label)"></div>
  <div class="abs" style="left:238px;top:167px;font-size:6.5px;font-weight:700">HalvernRidge.com</div>
  <div class="foot-name">HALVERN RIDGE</div><div class="page-no">2</div>
</section>

<!-- 3 Overview -->
<section class="slide" style="left:804px;top:6px">
  <div class="slide-head"><h2 class="slide-title">Overview</h2></div>
  <div class="card" style="left:20px;top:68px;width:108px;height:104px;padding:16px 8px">
    <div class="label" style="text-decoration:none">MANAGEMENT TEAM</div>
    <div style="margin-top:10px">Veteran Business Owners<br>&amp; Portfolio Manager</div>
    <div style="margin-top:17px;color:var(--label)">• OWEN R. TALBERT<br>• LUCAS D. BRENNER</div>
  </div>
  <div class="abs label" style="left:146px;top:57px;font-size:7px">STRATEGY</div>
  <div class="abs pale-box" style="left:144px;top:68px;width:102px;height:108px;padding:5px 6px;font-size:6.3px;line-height:1.3;border-bottom:1.5px solid var(--label)">Halvern Ridge, LLC seeks to take advantage of any Price-Value mismatch or Supply-Demand imbalance throughout the economy; ranging from economic industries and sectors, down to an individual business, security, or commodity.</div>
  <div class="abs label" style="left:260px;top:57px;font-size:7px">CORE FOCUS</div>
  <div class="abs pale-box" style="left:258px;top:68px;width:102px;height:108px;padding:5px 6px;font-size:6.3px;line-height:1.3;border-bottom:1.5px solid var(--label)">Undervalued/Overvalued securities, contracts, or other instruments; Looking for opportunities to capture significant value where intensive and proprietary fundamental, technical, and psychological research aligns with both established principles and sound logic.</div>
  <div class="foot-name">HALVERN RIDGE</div><div class="page-no">3</div>
</section>

<!-- 4 Why -->
<section class="slide" style="left:4px;top:238px">
  <div class="slide-head"><h2 class="slide-title">Why Halvern Ridge?&nbsp; A Disciplined Advantage</h2></div>
  <div class="abs" style="left:15px;top:57px;width:145px">
    <div class="label label-rule" style="width:145px">EXPERIENCED TEAM</div>
    <p class="body" style="margin-top:7px">Managing Members have more than 25 years combined experience across business management, financial markets, economics, research &amp; analytics.</p>
    <div class="label label-rule" style="width:145px;margin-top:12px">DISCIPLINED PROCESS</div>
    <p class="body" style="margin-top:7px">We follow a disciplined process based on established principles and sound logic in accordance with the scientific method.</p>
  </div>
  <div class="abs" style="left:188px;top:45px;width:195px">
    <div class="label" style="line-height:1.2">METHODICAL APPLICATION<br>OF KNOWLEDGE AND EXPERIENCE</div>
    <p class="body" style="margin-top:6px"><b>Elias Thornbury and Walter Ashcombe</b> respectively provide the description of our operating principles:</p>
  </div>
  <div class="abs pale-box quote-list body" style="left:186px;top:97px;width:196px;height:112px;padding:6px 6px">
    <p>"Industry and Patience are the Surest Means to Plenty."</p>
    <p>"An Investment in Knowledge Always Pays the Best Interest."</p>
    <p>"Risk Comes from not Knowing What You are Doing."</p>
    <p>"Investment is most Intelligent when It's most Business-Like."</p>
    <p>"Know What You are Doing; Know Your Business."</p>
  </div>
  <div class="foot-name">HALVERN RIDGE</div><div class="page-no">4</div>
</section>

<!-- 5 Why continued -->
<section class="slide" style="left:406px;top:238px">
  <div class="deco" style="left:180px;top:36px;width:212px;height:186px" role="img" aria-label="Faint pale blue technical pattern with a padlock motif"></div>
  <div class="slide-head"><h2 class="slide-title">Why Halvern Ridge? <small>(Continued)</small></h2></div>
  <div class="abs label" style="left:52px;top:60px">CONSISTENT RESULTS</div>
  <p class="abs body" style="left:52px;top:80px">Here again, <b>Walter Ashcombe</b> provides the clearest statement of our thinking…</p>
  <div class="abs pale-box" style="left:46px;top:102px;width:300px;height:38px;padding:5px 6px;font-size:7px;font-weight:700;line-height:1.3">"An investment operation is one which upon thorough analysis offers safety of principal and a satisfactory return; Operations not meeting these requirements are speculative."</div>
  <p class="abs body" style="left:52px;top:154px;width:290px">Halvern Ridge, LLC is targeting the consistent safety of principal and a satisfactory annual return.</p>
  <div class="foot-name">HALVERN RIDGE</div><div class="page-no">5</div>
</section>

<!-- 6 Disciplined Process -->
<section class="slide" style="left:806px;top:238px">
  <div class="slide-head"><h2 class="slide-title">Disciplined Process</h2></div>
  <div class="abs" style="left:16px;top:64px;width:150px">
    <div class="label label-rule" style="width:112px">COMMENTS ON THE PROCESS</div>
    <p class="body" style="margin-top:8px">We follow a disciplined process based on established principles and sound logic in accordance with the scientific method.</p>
    <p class="body" style="margin-top:5px">Each stage is reviewed against clear rules, results are measured, and the process is adjusted when new evidence shows a better path for capital.</p>
  </div>
  <svg class="abs" style="left:0;top:0" width="392" height="222" viewBox="0 0 392 222" aria-label="Cycle of five process stages">
    <defs>
      <marker id="cycle-head" viewBox="0 0 10 10" refX="5" refY="5" markerWidth="3" markerHeight="3" orient="auto">
        <polygon points="0,0 10,5 0,10" fill="#1b78de"/>
      </marker>
    </defs>
    <g fill="#bfe3f6">
      <circle cx="252" cy="32" r="30"/><circle cx="320" cy="88" r="28"/><circle cx="292" cy="152" r="29"/>
      <circle cx="212" cy="152" r="29"/><circle cx="186" cy="88" r="28"/>
    </g>
    <g fill="none" stroke="#1b78de" stroke-width="7" marker-end="url(#cycle-head)">
      <path d="M247.8 68.4 A24 24 0 0 1 275 88"/>
      <path d="M274.6 100.2 A24 24 0 0 1 242 113.5"/>
      <path d="M233.6 107.4 A24 24 0 0 1 238 72"/>
    </g>
  </svg>
  <div class="abs chart-text" style="left:228px;top:22px;width:48px">Experienced<br>Team</div>
  <div class="abs chart-text" style="left:296px;top:79px;width:48px">Targeted<br>Rate of<br>Return</div>
  <div class="abs chart-text" style="left:266px;top:144px;width:52px">Established<br>Principles</div>
  <div class="abs chart-text" style="left:186px;top:144px;width:52px">Monitoring<br>&amp; Reporting</div>
  <div class="abs chart-text" style="left:160px;top:83px;width:52px">Evaluation<br>&amp; Adaptation</div>
  <div class="foot-name">HALVERN RIDGE</div><div class="page-no">6</div>
</section>

<!-- 7 Organizational Structure -->
<section class="slide" style="left:4px;top:470px">
  <div class="slide-head"><h2 class="slide-title">Organizational Structure</h2></div>
  <div class="abs brand-name" style="left:0;width:392px;top:48px;text-align:center;font-size:12px">HALVERN RIDGE</div>
  <svg class="abs" style="left:0;top:0" width="392" height="222" aria-hidden="true">
    <g stroke="#1b78de" stroke-width="1.2" fill="none">
      <line x1="196" y1="66" x2="196" y2="76"/>
      <line x1="98" y1="76" x2="298" y2="76"/>
      <line x1="98" y1="76" x2="98" y2="83"/>
      <line x1="298" y1="76" x2="298" y2="83"/>
    </g>
  </svg>
  <div class="org-box" style="left:60px;top:83px;width:76px">LUCAS D. BRENNER<br>Chief Investment Officer</div>
  <div class="org-box" style="left:258px;top:83px;width:80px">OWEN R. TALBERT<br>Chief Development Officer</div>
  <ul class="bullets" style="left:20px;top:128px;width:170px">
    <li>13 YEARS EXPERIENCE</li>
    <li>2006 - 2018 Business Consultant, Manager, and VP across multiple organizations with various offerings ranging from technology and analytical assessments to cybersecurity and business continuity enhancements</li>
    <li>B.S. Westmoor University, 2006</li>
  </ul>
  <ul class="bullets" style="left:222px;top:128px;width:162px">
    <li>12 YEARS EXPERIENCE</li>
    <li>2012 - 2018 Senior Financial Advisor &amp; Senior Portfolio Manager at Crestline Securities</li>
    <li>2007 - 2012 Biology &amp; Applied Economics for Eastbrook University, Regional Service Corps, The Linden Foundation, The Greenfield Trust</li>
    <li>B.S. Eastbrook University, 2007 / M.S. Eastbrook University, 2012</li>
  </ul>
  <div class="foot-name">HALVERN RIDGE</div><div class="page-no">7</div>
</section>

<!-- 8 Investment Rationale -->
<section class="slide" style="left:406px;top:470px">
  <div class="deco" style="left:0;top:120px;width:392px;height:102px" role="img" aria-label="Faint pale blue pattern of interlocking gears and circuit lines"></div>
  <div class="slide-head"><h2 class="slide-title">Investment Rationale</h2></div>
  <div class="rationale-box" style="left:60px;top:52px;width:270px;height:52px;padding-top:3px">HALVERN RIDGE, LLC SEEKS TO TAKE ADVANTAGE OF ANY<br>PRICE-VALUE MISMATCH OR SUPPLY-DEMAND IMBALANCE<br>THROUGHOUT THE ECONOMY</div>
  <svg class="abs" style="left:0;top:0" width="392" height="222" aria-hidden="true">
    <g fill="#1b78de">
      <rect x="126" y="104" width="6" height="14"/><polygon points="117,116 141,116 129,128"/>
      <rect x="251" y="104" width="6" height="14"/><polygon points="242,116 266,116 254,128"/>
    </g>
  </svg>
  <div class="rationale-sub" style="left:79px;top:133px;width:100px;height:50px;padding-top:6px">ACROSS AND WITHIN<br>ECONOMIC SECTORS<br>AND INDUSTRIES</div>
  <div class="rationale-sub" style="left:198px;top:130px;width:110px;height:50px;padding-top:6px">UTILIZING INDIVIDUAL<br>SECURITIES, CONTRACTS,<br>AND COMMODITIES</div>
  <div class="foot-name">HALVERN RIDGE</div><div class="page-no">8</div>
</section>

<!-- 9 Process -->
<section class="slide" style="left:806px;top:470px">
  <div class="slide-head"><h2 class="slide-title">Process</h2></div>
  <div class="stage-head" style="left:30px;top:52px">STAGES 1-3</div>
  <div class="stage-head" style="left:146px;top:54px">STAGES 4-6</div>
  <div class="stage-head" style="left:262px;top:54px">EVALUATION</div>
  <svg class="abs" style="left:0;top:0" width="392" height="222" aria-hidden="true">
    <g fill="#2a86e8">
      <polygon points="30,68 58,68 66,82 58,96 30,96 37,82"/>
      <polygon points="64,68 92,68 100,82 92,96 64,96 71,82"/>
      <polygon points="98,68 126,68 134,82 126,96 98,96 105,82"/>
      <polygon points="146,68 174,68 182,82 174,96 146,96 153,82"/>
      <polygon points="180,68 208,68 216,82 208,96 180,96 187,82"/>
      <polygon points="214,68 234,68 242,82 234,96 214,96 221,82"/>
      <polygon points="262,71 344,71 344,66 360,82 344,98 344,93 262,93"/>
    </g>
  </svg>
  <div class="abs label" style="left:32px;top:101px;font-size:6px;line-height:1.15">STRATEGY, TECHNICALS,<br>&amp; IMPLEMENTATION</div>
  <div class="stage-box" style="left:30px;top:116px;width:108px;height:86px">
    <p>Strategic idea introduced along with tactical plans for implementing &amp; exiting the strategy.</p>
    <p>Fundamentals<br>and technicals confirmed.</p>
    <p>Position implemented/capital allocated.</p>
  </div>
  <div class="abs label" style="left:148px;top:108px;font-size:6px">MAINTENANCE</div>
  <div class="stage-box" style="left:146px;top:116px;width:106px;height:70px">
    <p>Each position is continuously scrutinized for strengths, weaknesses, opportunities, and threats (SWOT).</p>
    <p>Position held as long as fundamentals and technicals in-tact.</p>
  </div>
  <div class="abs label" style="left:264px;top:107px;font-size:6px">EVALUATE, ADAPT &amp; REPORT</div>
  <div class="stage-box" style="left:262px;top:116px;width:100px;height:70px">
    <p>Evaluate results of the entire process once a position is exited.</p>
    <p>Adapt any component of process as needed.</p>
    <p>Report candidly.</p>
  </div>
  <div class="foot-name">HALVERN RIDGE</div><div class="page-no">9</div>
</section>

</body>
</html>
```